KORBALT

The business want a professional looking business card. We have a scetch we will add but want the extra upgrade, and would like more suggestions for variations of our business cards.

```html
<!DOCTYPE html>
<html lang="en">
<head>
<meta charset="UTF-8">
<title>KORBALT Business Card</title>
<link href="https://fonts.googleapis.com/css2?family=Marcellus&family=Poppins:wght@400;500&display=swap" rel="stylesheet">
<style>
  :root {
    --backdrop-grey: #cccccc;
    --backdrop-gold-top: #a0661a;
    --backdrop-gold-mid: #8a5212;
    --backdrop-gold-low: #b98f42;
    --backdrop-gold-bottom: #e3d47a;
    --card: #2d2d2d;
    --gold: #b8913c;
    --gold-light: #e6d27c;
    --gold-deep: #9a6a22;
    --ink-light: #f2f2f2;
  }
  * { box-sizing: border-box; margin: 0; padding: 0; }
  html, body { width: 1200px; height: 1200px; overflow: hidden; }
  body {
    position: relative;
    background: var(--backdrop-grey);
    font-family: "Poppins", sans-serif;
  }
  .backdrop-gold {
    position: absolute; left: 600px; top: 0; width: 600px; height: 1200px;
    background: linear-gradient(180deg, var(--backdrop-gold-top) 0%, var(--backdrop-gold-mid) 25%, var(--backdrop-gold-low) 55%, var(--backdrop-gold-bottom) 100%);
  }
  .card {
    position: absolute; width: 732px; height: 418px;
    background: var(--card);
  }
  .card-front { left: 235px; top: 153px; }
  .card-back { left: 233px; top: 629px; }

  .person-icon { position: absolute; left: 54px; top: 69px; width: 24px; height: 24px; }
  .holder-title {
    position: absolute; left: 89px; top: 58px;
    font-family: "Marcellus", serif; font-size: 46px; line-height: 1; letter-spacing: 0.5px;
    background: linear-gradient(90deg, var(--gold-deep), var(--gold-light) 45%, var(--gold) 100%);
    -webkit-background-clip: text; background-clip: text; color: transparent;
  }
  .title-rule {
    position: absolute; left: 89px; top: 104px; width: 192px; height: 1.5px;
    background: linear-gradient(90deg, var(--gold-deep), var(--gold-light));
  }
  .role { position: absolute; left: 89px; top: 110px; font-size: 12.5px; color: var(--ink-light); }
  .person-name { position: absolute; left: 89px; top: 126px; font-size: 16.5px; color: var(--ink-light); }
  .divider-thick { position: absolute; left: 53px; top: 162px; width: 304px; height: 7px; background: var(--gold); }
  .divider-thin { position: absolute; left: 357px; top: 165px; width: 323px; height: 1.5px; background: var(--gold); }

  .contact-list { position: absolute; left: 53px; top: 232px; list-style: none; }
  .contact-item { display: flex; align-items: center; height: 44.5px; font-size: 21px; color: var(--ink-light); }
  .contact-item svg { width: 20px; height: 20px; margin-right: 16px; flex-shrink: 0; }

  .brand-front {
    position: absolute; left: 520px; top: 245px; width: 140px;
    display: flex; flex-direction: column; align-items: center; gap: 12px;
  }
  .brand-dot { width: 44px; height: 44px; border-radius: 50%; background: var(--gold); }
  .brand-name-small { font-family: "Marcellus", serif; font-size: 24px; letter-spacing: 2px; color: var(--gold); }

  .brand-back {
    position: absolute; left: 0; top: 0; width: 100%; height: 100%;
    display: flex; flex-direction: column; align-items: center;
  }
  .brand-back .brand-dot { width: 90px; height: 90px; margin-top: 126px; }
  .brand-name-large {
    margin-top: 42px; font-family: "Marcellus", serif; font-size: 38px; line-height: 1;
    letter-spacing: 13px; padding-left: 13px; color: var(--ink-light);
  }
  .brand-since { margin-top: 10px; font-size: 12px; font-weight: 500; letter-spacing: 7px; padding-left: 7px; color: var(--ink-light); }
</style>
</head>
<body>
  <div class="backdrop-gold"></div>

  <section class="card card-front">
    <svg class="person-icon" viewBox="0 0 24 24" aria-hidden="true">
      <circle cx="12" cy="6.5" r="5" fill="#d9c06a"/>
      <path d="M1 24 C1 16 6 13 12 13 C18 13 23 16 23 24 Z" fill="#c6a04c"/>
    </svg>
    <h1 class="holder-title">KORBALT L INDQVIST</h1>
    <div class="title-rule"></div>
    <p class="role">CEO &amp; Founder</p>
    <p class="person-name">Arne Halvor Lindqvist</p>
    <div class="divider-thick"></div>
    <div class="divider-thin"></div>

    <ul class="contact-list">
      <li class="contact-item">
        <svg viewBox="0 0 24 24" aria-hidden="true"><path d="M6.6 2.5 L9.5 6.8 L7.6 9 C8.8 11.8 11.8 14.8 15 16.4 L17.2 14.5 L21.5 17.4 L19.6 21.5 C11 21 3 13 2.5 4.4 Z" fill="#c6a04c"/></svg>
        +004791236470
      </li>
      <li class="contact-item">
        <svg viewBox="0 0 24 24" aria-hidden="true"><rect x="1" y="4.5" width="22" height="15" fill="#c6a04c"/><path d="M1 4.5 L12 13 L23 4.5 M1 19.5 L9 11.5 M23 19.5 L15 11.5" stroke="#2d2d2d" stroke-width="1.4" fill="none"/></svg>
        korbalt.llc@mailbox.com
      </li>
      <li class="contact-item">
        <svg viewBox="0 0 24 24" aria-hidden="true" fill="none" stroke="#c6a04c" stroke-width="1.6"><circle cx="12" cy="12" r="10"/><ellipse cx="12" cy="12" rx="4.5" ry="10"/><path d="M2 12 H22 M4 6.5 H20 M4 17.5 H20 M12 2 V22"/></svg>
        www.korbalt.llc
      </li>
    </ul>

    <div class="brand-front">
      <span class="brand-dot"></span>
      <span class="brand-name-small">KORBALT</span>
    </div>
  </section>

  <section class="card card-back">
    <div class="brand-back">
      <span class="brand-dot"></span>
      <p class="brand-name-large">KORBALT</p>
      <p class="brand-since">SINCE 2026</p>
    </div>
  </section>
</body>
</html>
```